Modern Banner and Window Decal Design For Law Firm Lawyer

We are looking for three modern and sophisticated banner design and window decal for our law firm.

Banner measurements/types:

1) Height: 130 cm Width: 160 cm (Outdoor banner)
2) Height: 200 cm Width: 85 cm (Pull up/retractable indoor banner)

Window Decal:
3) Height: 70cm width 70cm

Our law firm is based in Melbourne, Australia and we deal with property law mostly.

We prefer a white background with classic text in black or grey. We would also like a dash of colour so please use a green, blue or aqua colour palette that is consistent with our logo. Vector attached. A nice photo of property, Melbourne city viee, or family home would be nice.

We do not want any law related images - scales of justice, gavel or the like.

Our ultimate goal is to communicate that the firm is modern, professional and knowledgeable

We would like the following:

1. Our logo
2. Our services: - Property Law - Wills - Powers of Attorney - Probate - Estate Administration - Consultancy & Agency
3. Phone number
4. Web Address

5. For pull up/retractable banner we would also like the following text:

We use the latest digital technology and fixed-fees to provide fast and affordable legal advice that is easy to understand.

For privacy reasons, we will provide business details once we have decided on the winner.

We will monitor entries closely and promise to provide feedback and guidance on each entry.

Thank you very much for considering this project.

Target Market(s)

General public, professionals, lawyers and conveyancers

Industry/Entity Type

Law Firm

Font styles to use
Sans Serif

Colors
0393ce
34a6d7
0456a4
3176b5
acd037
33b8a4
86cfc6
00a990
9ccb3b

Requirements
Must have
• 1. Our logo
• 2. Our services: - Property Law - Wills - Powers of Attorney - Probate & Estate Administration - Consultancy & Agency
• 3. Phone number
• 4. Web Address
Nice to have
• Picture of Melbourne, Australia city ; property/buildings/lawyers
Should not have
• We do not want any law related images - scales of justice, gavel or the like.

```html
<!DOCTYPE html>
<html lang="en">
<head>
<meta charset="utf-8">
<title>Ridgeline Lawyers – Pull-up Banner</title>
<link rel="stylesheet" href="https://fonts.googleapis.com/css2?family=Montserrat:wght@500;700&family=Roboto+Condensed:wght@700&display=swap">
<style>
  :root {
    --backdrop: #ededed;
    --paper: #ffffff;
    --ink: #3c3f44;
    --ink-soft: #55585d;
    --teal: #00a990;
    --teal-light: #33b8a4;
    --blue: #0393ce;
    --blue-mid: #3176b5;
    --blue-deep: #0456a4;
  }
  * { box-sizing: border-box; margin: 0; padding: 0; }
  html, body {
    width: 1200px; height: 900px; overflow: hidden;
    background: var(--backdrop);
  }
  .canvas {
    position: relative; width: 1200px; height: 900px;
  }
  .banner {
    position: absolute; left: 430px; top: 20px;
    width: 340px; height: 860px;
    background: var(--paper);
    box-shadow: 0 2px 10px rgba(0,0,0,0.08);
    overflow: hidden;
  }
  .brand {
    position: absolute; left: 22px; top: 34px;
    display: flex; align-items: center; gap: 16px;
  }
  .brand-mark {
    width: 92px; height: 92px; border-radius: 50%;
    background: var(--blue);
    flex: none;
  }
  .brand-name {
    font-family: "Montserrat", sans-serif;
    font-weight: 500;
    color: var(--ink);
    font-size: 26px;
    line-height: 1.1;
    letter-spacing: 0.5px;
  }
  .brand-name span { display: block; }
  .brand-name .sub { font-size: 19px; letter-spacing: 1px; }
  .feature-art {
    position: absolute; left: 0; top: 118px;
    width: 340px; height: 470px;
    display: block;
  }
  .services {
    position: absolute; left: 0; top: 596px; width: 340px;
    text-align: center;
  }
  .services-title {
    font-family: "Montserrat", sans-serif;
    font-weight: 700;
    font-size: 18px;
    color: var(--teal);
    letter-spacing: 0.3px;
    margin-bottom: 4px;
  }
  .services-list { list-style: none; }
  .services-list li {
    font-family: "Roboto Condensed", sans-serif;
    font-weight: 700;
    font-size: 23px;
    line-height: 27px;
    color: var(--ink-soft);
    letter-spacing: -0.3px;
  }
  .services-list li::before {
    content: "\2713";
    color: var(--teal);
    margin-right: 4px;
    font-size: 20px;
  }
  .divider {
    position: absolute; left: 14px; right: 14px; top: 766px;
    height: 3px; background: var(--teal);
  }
  .contact {
    position: absolute; left: 0; width: 340px;
    display: flex; justify-content: center; align-items: center; gap: 6px;
    font-family: "Montserrat", sans-serif;
    font-weight: 700;
    color: var(--teal);
    font-size: 19px;
  }
  .contact-phone { top: 782px; }
  .contact-web { top: 814px; }
  .contact-icon { width: 24px; height: 24px; flex: none; }
</style>
</head>
<body>
<div class="canvas">
  <div class="banner">
    <div class="brand">
      <div class="brand-mark"></div>
      <div class="brand-name"><span>RIDGELINE</span><span class="sub">LAWYERS</span></div>
    </div>

    <svg class="feature-art" viewBox="0 0 340 470" xmlns="http://www.w3.org/2000/svg">
      <defs>
        <linearGradient id="city-tone" x1="0" y1="0" x2="0" y2="1">
          <stop offset="0" stop-color="#6fa8d8"/>
          <stop offset="0.55" stop-color="#a9c6dc"/>
          <stop offset="1" stop-color="#4b5f72"/>
        </linearGradient>
        <linearGradient id="home-tone" x1="0" y1="0" x2="0" y2="1">
          <stop offset="0" stop-color="#a7a6cc"/>
          <stop offset="0.5" stop-color="#4a5068"/>
          <stop offset="1" stop-color="#6b6f78"/>
        </linearGradient>
        <linearGradient id="band-blue" x1="0" y1="0" x2="1" y2="0">
          <stop offset="0" stop-color="#0456a4"/>
          <stop offset="1" stop-color="#34a6d7"/>
        </linearGradient>
      </defs>
      <polygon class="band-teal" points="0,70 340,0 340,18 0,86" fill="#00a990"/>
      <polygon class="band-blue" points="0,86 260,32 200,62 0,112" fill="url(#band-blue)"/>
      <g role="img" aria-label="Photo of the Melbourne city skyline with tall towers under a blue sky">
        <polygon points="0,120 340,40 340,225 0,290" fill="url(#city-tone)"/>
      </g>
      <polygon class="band-blue" points="0,290 340,225 340,246 0,306" fill="url(#band-blue)"/>
      <polygon class="band-teal" points="0,306 340,246 340,254 0,316" fill="#33b8a4"/>
      <g role="img" aria-label="Photo of a modern two-storey family home with a double garage at dusk">
        <polygon points="0,316 340,254 340,400 0,455" fill="url(#home-tone)"/>
      </g>
      <polygon class="band-blue" points="0,455 340,400 340,414 0,470" fill="url(#band-blue)"/>
      <polygon class="band-teal" points="160,441 340,414 340,424 130,456" fill="#00a990"/>
    </svg>

    <section class="services">
      <h2 class="services-title">OUR SERVICES</h2>
      <ul class="services-list">
        <li>Property Law</li>
        <li>Wills</li>
        <li>Powers of Attorney</li>
        <li>Probate &amp; Estate Administration</li>
        <li>Consultancy &amp; Agency</li>
      </ul>
    </section>

    <div class="divider"></div>

    <div class="contact contact-phone">
      <svg class="contact-icon" viewBox="0 0 24 24" aria-hidden="true">
        <circle cx="12" cy="12" r="12" fill="var(--teal)"/>
        <path d="M8.6 6.2c.4-.3.9-.2 1.2.2l1.3 1.9c.3.4.2.9-.2 1.2l-.9.7c.6 1.4 1.7 2.6 3.1 3.3l.7-.9c.3-.4.8-.5 1.2-.2l1.9 1.3c.4.3.5.8.2 1.2l-.8 1.1c-.4.5-1 .7-1.6.5-3.5-1.1-6.2-3.8-7.2-7.3-.2-.6 0-1.2.5-1.6z" fill="#fff"/>
      </svg>
      <span>(55) 9999.9999</span>
    </div>

    <div class="contact contact-web">
      <svg class="contact-icon" viewBox="0 0 24 24" aria-hidden="true">
        <circle cx="12" cy="12" r="12" fill="var(--teal)"/>
        <g fill="none" stroke="#fff" stroke-width="1.4">
          <circle cx="12" cy="12" r="6.5"/>
          <ellipse cx="12" cy="12" rx="2.8" ry="6.5"/>
          <line x1="5.5" y1="12" x2="18.5" y2="12"/>
        </g>
      </svg>
      <span>www.website.com</span>
    </div>
  </div>
</div>
</body>
</html>
```